Nonprofit needs table front banner

Open Lantern is a disability advocacy organization in Indiana. We are requesting a graphic design for a table front banner 28 inches high and 72 inches long. The banner must incorporate Open Lantern’s logo, and the logos of our two web projects, Riverlark and Zestlink. (See attached items.) We would also like the banner to incorporate our slogan, and the slogans of Riverlark and Zestlink:

• Riverlark slogan: “Searching for Support on the Web Can Feel Like Wandering Through Thick Fog. But with Riverlark, Now You Have a Lighthouse.”

• Open Lantern slogan: “Indiana’s Source for Disability News and Information”

• Zestlink slogan: “Where Workers with Disabilities and Inclusive Employers Connect!”

As Open Lantern is the organization and Riverlark and Zestlink are our projects, we would like Open Lantern’s logo and slogan to be in the middle, and slightly more prominent. Also, as we are a disability organization, the banner should be designed with basic accessibility in mind. This means large text in a clear font, with good contrast between the text and the background. The text should be in a sans serif font that is clear and easy to read, with no italics or script fonts. There should not be a "busy" picture or pattern behind the text.

Industry/Entity Type

Non-Profit

Font styles to use
Sans Serif

Requirements
Must have
• The banner must incorporate Open Lantern’s logo, and the logos of our two web projects, Riverlark and Zestlink. (See attached items.) We would also like the banner to incorporate our slogan, and the slogans of Riverlark and Zestlink:
• • Riverlark slogan: “Searching for Support on the Web Can Feel Like Wandering Through Thick Fog. But with Riverlark, Now You Have a Lighthouse.”
• • Open Lantern slogan: “Indiana’s Source for Disability News and Information”
• • Zestlink slogan: “Where Workers with Disabilities and Inclusive Employers Connect!”
Nice to have
• As Open Lantern is the organization and Riverlark and Zestlink are our projects, we would like Open Lantern’s logo and slogan to be in the middle, and slightly more prominent.
Should not have
• No italics or script fonts. There should not be a "busy" picture or pattern behind the text.

```html
<!DOCTYPE html>
<html lang="en">
<head>
<meta charset="utf-8">
<title>Open Lantern – Table Banner</title>
<link rel="stylesheet" href="https://fonts.googleapis.com/css2?family=Poppins:wght@300;600&display=swap">
<style>
  :root {
    --brand-blue: #2c56a3;
    --paper: #ffffff;
    --frame: #1a1a1a;
    --on-blue: #ffffff;
  }
  * { margin: 0; padding: 0; box-sizing: border-box; }
  html, body { width: 1200px; height: 466px; overflow: hidden; background: var(--paper); }
  .banner {
    position: relative;
    width: 1200px;
    height: 466px;
    background: var(--paper);
    border: 1px solid var(--frame);
    overflow: hidden;
    font-family: "Poppins", sans-serif;
  }
  .banner-shapes { position: absolute; inset: 0; width: 100%; height: 100%; }
  .org-mark {
    position: absolute;
    left: 0; right: 0; top: 40px;
    display: flex; flex-direction: column; align-items: center;
  }
  .org-mark-dot {
    width: 112px; height: 112px;
    border-radius: 50%;
    background: var(--brand-blue);
  }
  .org-name {
    margin-top: 26px;
    font-size: 44px; font-weight: 600;
    line-height: 1;
    color: var(--brand-blue);
  }
  .org-slogan {
    position: absolute;
    left: 0; right: 0; top: 265px;
    text-align: center;
    font-size: 37px; font-weight: 600;
    letter-spacing: -0.2px;
    color: var(--brand-blue);
  }
  .project {
    position: absolute;
    top: 340px;
    color: var(--on-blue);
  }
  .project-riverlark { left: 88px; width: 600px; }
  .project-zestlink { left: 742px; width: 400px; }
  .project-slogan {
    font-size: 15.5px; font-weight: 300;
    line-height: 25px;
  }
  .project-name {
    display: flex; align-items: center; gap: 10px;
    margin-top: 24px;
    font-size: 24px; font-weight: 300;
    line-height: 1;
  }
  .project-dot {
    width: 32px; height: 32px; border-radius: 50%;
    background: var(--on-blue);
  }
  .project-square {
    width: 28px; height: 28px;
    background: var(--on-blue);
  }
</style>
</head>
<body>
<main class="banner">
  <svg class="banner-shapes" viewBox="0 0 1500 583" preserveAspectRatio="none" aria-hidden="true">
    <!-- corner blades -->
    <path fill="var(--brand-blue)" d="M0 0 H292 Q150 50 0 118 Z"/>
    <path fill="var(--brand-blue)" d="M0 150 Q120 112 242 106 Q110 150 0 228 Z"/>
    <path fill="var(--brand-blue)" d="M0 255 Q70 238 132 228 Q60 260 0 292 Z"/>
    <!-- lower band -->
    <rect fill="var(--brand-blue)" x="0" y="390" width="1500" height="193"/>
    <path fill="var(--brand-blue)" d="M1440 390 Q1480 382 1500 374 V390 Z"/>
    <!-- right blades in band -->
    <path fill="var(--paper)" d="M1380 440 Q1450 410 1500 392 V402 Q1450 420 1380 440 Z"/>
    <path fill="var(--paper)" d="M1290 583 Q1400 500 1500 470 V583 Z"/>
  </svg>

  <header class="org-mark">
    <div class="org-mark-dot"></div>
    <div class="org-name">Open Lantern</div>
  </header>

  <h1 class="org-slogan">Indiana’s Source for Disability News and Information</h1>

  <section class="project project-riverlark">
    <p class="project-slogan">Searching for Support on the Web Can Feel Like Wandering Through Thick Fog.<br>But with Riverlark, Now You Have a Lighthouse.</p>
    <div class="project-name"><span class="project-dot"></span>Riverlark</div>
  </section>

  <section class="project project-zestlink">
    <p class="project-slogan">Where Workers with Disabilities and Inclusive<br>Employers Connect!</p>
    <div class="project-name"><span class="project-square"></span>Zestlink</div>
  </section>
</main>
</body>
</html>
```